Pellworth and Tasker Ranch Insurance

Would like you all to design a logo for our Business cards and possible letterhead.
This business provides Ranch insurance for folks in Texas, New Mexico, and Oklahoma

Ggood stuff everybody, be sure to include email and Mobil for both of us on all designs

Thanks

Hello All

Wanted to let you all know i am going to extend deadline a few days, and add some more $$ to the budget

Reason: Give everybody a bit ,more time, and I added more money

Appreciate all of yalls hard work, will review and provide feed back hopefully today, been a little whacky with the holidays and all

Industry/Entity Type

Business

```html
<!DOCTYPE html>
<html lang="en">
<head>
<meta charset="utf-8">
<title>Pellworth and Tasker – Letterhead and Business Card</title>
<link rel="stylesheet" href="https://fonts.googleapis.com/css2?family=Quicksand:wght@500;600;700&family=Arimo:wght@400;700&display=swap">
<style>
  :root {
    --backdrop: #999999;
    --paper: #ffffff;
    --brand-red: #e3110f;
    --brand-red-deep: #b80506;
    --brand-red-light: #ff3b33;
    --ink: #111111;
    --ink-soft: #222222;
    --band-black: #141414;
    --watermark: #fbe3e3;
  }
  * { box-sizing: border-box; margin: 0; padding: 0; }
  html, body {
    width: 1200px; height: 1000px; overflow: hidden;
    background: var(--backdrop);
  }
  .canvas { position: relative; width: 1200px; height: 1000px; }

  /* Letterhead */
  .letterhead {
    position: absolute; left: 90px; top: 140px;
    width: 480px; height: 710px;
    background: var(--paper);
  }
  .letterhead__top-band {
    position: absolute; left: 0; top: 0; width: 100%; height: 38px;
    background: linear-gradient(100deg, var(--brand-red-deep) 0%, var(--brand-red) 35%, var(--brand-red-light) 55%, var(--brand-red) 75%, var(--brand-red-deep) 100%);
  }
  .letterhead__header {
    position: absolute; left: 0; top: 38px; width: 100%; height: 112px;
  }
  .brand-mark {
    display: flex; align-items: center; gap: 10px;
    font-family: "Quicksand", sans-serif; font-weight: 600; color: var(--ink);
  }
  .brand-mark__dot {
    flex: none; border-radius: 50%; background: var(--brand-red);
  }
  .letterhead .brand-mark { position: absolute; left: 18px; top: 30px; font-size: 27px; }
  .letterhead .brand-mark__dot { width: 38px; height: 38px; }
  .letterhead__label {
    position: absolute; right: 40px; top: 82px;
    font-family: "Arimo", sans-serif; font-weight: 700; font-size: 13px; color: var(--ink-soft);
  }
  .letterhead__rule {
    position: absolute; left: 0; width: 100%; height: 12px;
    background: linear-gradient(180deg, var(--brand-red-light), var(--brand-red) 50%, var(--brand-red-deep));
  }
  .letterhead__rule--top { top: 150px; }
  .letterhead__rule--bottom { top: 590px; }
  .letterhead__watermark {
    position: absolute; left: 40px; top: 410px; width: 400px; height: 160px;
    display: flex; align-items: center; justify-content: center;
    font-family: "Quicksand", sans-serif; font-weight: 700; font-size: 60px;
    color: var(--watermark);
  }
  .letterhead__footer {
    position: absolute; left: 0; top: 602px; width: 100%; height: 108px;
    font-family: "Quicksand", sans-serif; font-weight: 600; font-size: 10.5px; color: var(--ink);
  }
  .letterhead__web { position: absolute; left: 26px; top: 18px; line-height: 18px; }
  .letterhead__address { position: absolute; right: 30px; top: 50px; line-height: 20px; text-align: right; }

  /* Business card */
  .business-card {
    position: absolute; left: 640px; top: 420px;
    width: 420px; height: 250px;
    background: var(--paper); overflow: hidden;
  }
  .business-card__head { position: absolute; left: 0; top: 0; width: 100%; height: 118px; }
  .business-card .brand-mark { position: absolute; left: 34px; top: 44px; font-size: 22px; }
  .business-card .brand-mark__dot { width: 32px; height: 32px; }
  .business-card__black-band {
    position: absolute; left: 0; top: 118px; width: 100%; height: 12px; background: var(--band-black);
  }
  .business-card__body {
    position: absolute; left: 0; top: 130px; width: 100%; height: 120px;
    background: linear-gradient(105deg, var(--brand-red-deep) 0%, var(--brand-red) 30%, var(--brand-red-light) 50%, var(--brand-red) 70%, var(--brand-red-deep) 100%);
    font-family: "Arimo", sans-serif; font-size: 11.5px; color: var(--paper);
  }
  .contact-list { position: absolute; left: 32px; top: 20px; list-style: none; }
  .contact-list li { height: 23px; display: flex; align-items: center; gap: 6px; }
  .contact-list .phone-icon { width: 12px; height: 17px; }
  .business-card__people {
    position: absolute; right: 34px; top: 28px; text-align: center;
  }
  .business-card__names { font-size: 13px; text-decoration: underline; }
  .business-card__role { font-size: 11px; margin-top: 4px; }
</style>
</head>
<body>
<main class="canvas">

  <section class="letterhead" aria-label="Letterhead">
    <div class="letterhead__top-band"></div>
    <header class="letterhead__header">
      <div class="brand-mark"><span class="brand-mark__dot"></span><span>Pellworth and Tasker</span></div>
      <span class="letterhead__label">LetterHead</span>
    </header>
    <div class="letterhead__rule letterhead__rule--top"></div>
    <div class="letterhead__watermark" aria-hidden="true">Pellworth and Tasker</div>
    <div class="letterhead__rule letterhead__rule--bottom"></div>
    <footer class="letterhead__footer">
      <div class="letterhead__web">
        <p>Website:&nbsp; www.pellworthandtasker.com</p>
        <p>Email:&nbsp; p&amp;t@pellworthandtasker.com</p>
      </div>
      <div class="letterhead__address">
        <p># 408 W Cedar St. Marlow, TX 76833</p>
        <p>Phone:&nbsp; 325.555.0147</p>
      </div>
    </footer>
  </section>

  <section class="business-card" aria-label="Business card">
    <div class="business-card__head">
      <div class="brand-mark"><span class="brand-mark__dot"></span><span>Pellworth and Tasker</span></div>
    </div>
    <div class="business-card__black-band"></div>
    <div class="business-card__body">
      <ul class="contact-list">
        <li>
          <svg class="phone-icon" viewBox="0 0 12 17" aria-hidden="true">
            <rect x="1" y="0.5" width="10" height="16" rx="2" fill="#222" stroke="#ddd" stroke-width="1"/>
            <rect x="2.8" y="2.5" width="6.4" height="7" fill="#888"/>
          </svg>
          <span>325.555.0147</span>
        </li>
        <li>Email:&nbsp; p&amp;t@pellworthandtasker.com</li>
        <li>Website:&nbsp; www.pellworthandtasker.com</li>
        <li># 408 W Cedar St. Marlow, TX 76833</li>
      </ul>
      <div class="business-card__people">
        <p class="business-card__names">Pellworth &amp; Tasker</p>
        <p class="business-card__role">Directors</p>
      </div>
    </div>
  </section>

</main>
</body>
</html>
```